Stationery Design Project

We need a Stationery Design for automotive industry.
Updates

Target Market(s)

Mechanic garage and Mechanics

Industry/Entity Type

Automotive

Requirements
Must have
• The logo company and the legal information.

We are a car spart parts and tools delar
Nice to have
• We like something elegant and simple.

```html
<!DOCTYPE html>
<html lang="en">
<head>
<meta charset="utf-8">
<title>Northline Auto Parts — Stationery</title>
<link href="https://fonts.googleapis.com/css2?family=Jost:wght@400;500;600&display=swap" rel="stylesheet">
<style>
  :root{
    --bg:#ffffff;
    --paper:#ffffff;
    --ink:#111111;
    --band:#0c0c0c;
    --band-mid:#2a2a2a;
    --chrome:#c9ccd0;
    --muted:#9a9a9a;
    --white:#ffffff;
  }
  *{margin:0;padding:0;box-sizing:border-box}
  html,body{width:1200px;height:1122px;overflow:hidden;background:var(--bg)}
  body{position:relative;font-family:"Jost",sans-serif;color:var(--ink)}

  .sheet{position:absolute;background:var(--paper);border:1px solid #e2e2e2;overflow:hidden}

  .band{position:absolute;left:0;right:0;
    background:
      radial-gradient(ellipse 140px 10px at 85% 38%, rgba(255,255,255,.85), rgba(255,255,255,0) 70%),
      linear-gradient(180deg,var(--band-mid) 0%,var(--band) 45%,#000 100%);}
  .rule{position:absolute;left:0;right:0;
    background:linear-gradient(180deg,#000 0%,#000 30%,var(--chrome) 45%,#000 60%,#000 100%);}

  .brand{position:absolute;color:var(--white);font-weight:500;letter-spacing:.18em;text-transform:uppercase;white-space:nowrap}

  /* letterhead */
  .letterhead{left:69px;top:69px;width:663px;height:858px}
  .letterhead .band{top:35px;height:72px}
  .letterhead .rule{top:110px;height:18px}
  .letterhead .brand{left:60px;top:62px;font-size:18px}
  .letterhead .footer-rule{position:absolute;left:0;right:0;top:825px;height:21px;
    background:linear-gradient(180deg,var(--chrome) 0%,#000 20%,#111 70%,var(--chrome) 100%)}
  .legal{position:absolute;right:46px;top:146px;text-align:right;font-size:8.5px;letter-spacing:.12em;line-height:14px;font-style:normal}
  .legal .company{font-size:10.5px;font-weight:600;letter-spacing:.14em;margin-bottom:3px}

  /* business cards */
  .card{width:308px;height:183px}
  .card-front{left:787px;top:99px;background:linear-gradient(180deg,#2b2b2b 0%,#0d0d0d 60%,#000 100%);border-color:#000}
  .card-front .brand{left:0;right:0;top:66px;text-align:center;font-size:14px}
  .card-front .rule{top:128px;height:3px;background:linear-gradient(90deg,#000,var(--chrome) 60%,#000)}
  .card-front .rule.low{top:177px}
  .card-front .web{position:absolute;left:0;right:0;top:156px;text-align:center;color:var(--muted);font-size:6.5px;letter-spacing:.6em;white-space:nowrap}
  .card-back{left:787px;top:313px;background:linear-gradient(180deg,#fff 0%,#ececec 100%)}
  .card-back .strip{position:absolute;left:0;right:0;top:106px;height:34px;background:#000;border-top:2px solid var(--chrome);border-bottom:2px solid var(--chrome);color:var(--white);font-size:6.5px;font-weight:500;letter-spacing:.1em;text-align:center;line-height:12px;padding-top:4px;white-space:nowrap}
  .card-back .web{position:absolute;left:0;right:0;top:155px;text-align:center;color:#555;font-size:6.5px;letter-spacing:.6em;white-space:nowrap}

  /* envelope */
  .envelope{left:434px;top:597px;width:705px;height:360px}
  .envelope .band{top:231px;height:73px}
  .envelope .rule{top:307px;height:18px}
  .envelope .brand{left:56px;top:258px;font-size:14px}
  .envelope .return{position:absolute;right:40px;top:244px;text-align:right;color:var(--chrome);font-size:8px;letter-spacing:.07em;line-height:14px;font-style:normal;white-space:nowrap}
  .envelope .return .company{font-size:10px;font-weight:600;letter-spacing:.12em}
</style>
</head>
<body>

<section class="sheet letterhead" aria-label="Letterhead">
  <div class="band"></div>
  <div class="rule"></div>
  <div class="brand">Northline Auto Parts</div>
  <address class="legal">
    <div class="company">NORTHLINE AUTO PARTS PTY LTD.</div>
    <div>ABN:48 302 774 519</div>
    <div>P.O. BOX 412 PARRAMATTA NSW</div>
    <div>PHONE 00 2468 135</div>
    <div>WWW.NORTHLINEAUTOPARTS.COM.AU</div>
    <div>hello@northlineautoparts.com.au</div>
  </address>
  <div class="footer-rule"></div>
</section>

<section class="sheet card card-front" aria-label="Business card front">
  <div class="brand">Northline Auto Parts</div>
  <div class="rule"></div>
  <div class="web">WWW.NORTHLINEAUTOPARTS.COM.AU</div>
  <div class="rule low"></div>
</section>

<section class="sheet card card-back" aria-label="Business card back">
  <div class="strip">
    <div>ABN:48 302 774 519 P.O. BOX 412 PARRAMATTA NSW</div>
    <div>PHONE 00 2468 135 &nbsp; | &nbsp; hello@northlineautoparts.com.au</div>
  </div>
  <div class="web">WWW.NORTHLINEAUTOPARTS.COM.AU</div>
</section>

<section class="sheet envelope" aria-label="Envelope">
  <div class="band"></div>
  <div class="rule"></div>
  <div class="brand">Northline Auto Parts</div>
  <address class="return">
    <div class="company">NORTHLINE AUTO PARTS PTY LTD</div>
    <div>ABN:48 302 774 519 P.O. BOX 412 PARRAMATTA NSW</div>
    <div>PHONE 00 2468 135 &nbsp;|&nbsp; WWW.NORTHLINEAUTOPARTS.COM.AU</div>
    <div>hello@northlineautoparts.com.au</div>
  </address>
</section>

</body>
</html>
```